Maple Hollow Bloom Panels Business card

Looking to have a business card design incorporating my logo for my flower wall business.

Industry/Entity Type

Wedding & event planning

Contact Information for Business Card

My business logo, my name - Lena Whitcombe (owner), my tagline - Let us be your something extra, phone # 401-726-3148, email address - maplehollowbloompanels@mailvane.net, my website - maplehollowbloompanels.net, Instagram handle- @maplehollowbloompanels, FB handle Handle - maplehollowbloompanels

Font styles to use
Other font styles liked:
• Sentaina is the font that is used in my logo

Requirements
Must have
• Would like a double sided business card

```html
<!DOCTYPE html>
<html lang="en">
<head>
<meta charset="utf-8">
<title>Maple Hollow Bloom Panels – Business Card</title>
<link rel="stylesheet" href="https://fonts.googleapis.com/css2?family=Cormorant+Garamond:wght@400;500&family=Mrs+Saint+Delafield&display=swap">
<style>
  :root {
    --page-bg: #fdfdfd;
    --card-pink: #fce0eb;
    --card-white: #ffffff;
    --ink: #2b2b2b;
    --accent-pink: #d0479a;
    --ring-white: #fffafc;
    --shadow: rgba(0, 0, 0, 0.16);
  }
  * { margin: 0; padding: 0; box-sizing: border-box; }
  html, body {
    width: 1200px;
    height: 900px;
    overflow: hidden;
    background: var(--page-bg);
  }
  .canvas {
    position: relative;
    width: 1200px;
    height: 900px;
    font-family: "Cormorant Garamond", Georgia, serif;
    color: var(--ink);
  }
  .card {
    position: absolute;
    top: 300px;
    width: 525px;
    height: 301px;
    box-shadow: 0 14px 40px var(--shadow);
  }
  .card--front { left: 56px; background: var(--card-pink); }
  .card--back  { left: 620px; background: var(--card-white); }

  /* Front */
  .front-badge {
    position: absolute;
    left: 179px;
    top: 69px;
    width: 168px;
    height: 168px;
    border-radius: 50%;
    background: var(--ring-white);
    display: flex;
    align-items: center;
    justify-content: center;
  }
  .front-badge__name {
    font-size: 19px;
    font-weight: 400;
    line-height: 1.15;
    text-align: center;
    color: var(--ink);
    width: 130px;
  }
  .front-website {
    position: absolute;
    left: 0;
    right: 0;
    top: 263px;
    text-align: center;
    font-size: 12.5px;
  }

  /* Back */
  .back-brand {
    position: absolute;
    left: 0;
    right: 0;
    top: 40px;
    text-align: center;
    font-size: 20px;
    font-weight: 400;
    letter-spacing: 0.5px;
  }
  .holder-name {
    position: absolute;
    left: 0;
    right: 0;
    top: 110px;
    text-align: center;
    font-size: 27px;
    font-weight: 500;
    letter-spacing: 0.3px;
    line-height: 1;
  }
  .holder-role {
    position: absolute;
    left: 0;
    right: 0;
    top: 143px;
    text-align: center;
    font-size: 12.5px;
    letter-spacing: 0.3px;
    line-height: 1;
  }
  .tagline {
    position: absolute;
    left: 0;
    right: 0;
    top: 148px;
    text-align: center;
    font-family: "Mrs Saint Delafield", cursive;
    font-size: 40px;
    color: var(--accent-pink);
    line-height: 1;
  }
  .contact-list {
    position: absolute;
    top: 246px;
    list-style: none;
    font-size: 10.5px;
    line-height: 1;
  }
  .contact-list--left  { left: 51px; }
  .contact-list--right { left: 289px; }
  .contact-list li {
    display: flex;
    align-items: center;
    height: 17px;
  }
  .contact-icon {
    width: 13px;
    height: 13px;
    margin-right: 8px;
    flex: none;
  }
  .social-mark {
    width: 12px;
    height: 12px;
    margin-right: 8px;
    border-radius: 2px;
    background: var(--ink);
    flex: none;
  }
  .contact-divider {
    position: absolute;
    left: 262px;
    top: 247px;
    width: 1px;
    height: 33px;
    background: var(--accent-pink);
  }
</style>
</head>
<body>
<main class="canvas">

  <section class="card card--front" aria-label="Business card front">
    <div class="front-badge">
      <p class="front-badge__name">Maple Hollow Bloom Panels</p>
    </div>
    <p class="front-website">www.maplehollowbloompanels.net</p>
  </section>

  <section class="card card--back" aria-label="Business card back">
    <p class="back-brand">Maple Hollow Bloom Panels</p>
    <h1 class="holder-name">LENA WHITCOMBE</h1>
    <p class="holder-role">OWNER</p>
    <p class="tagline">Let us be your something extra</p>

    <ul class="contact-list contact-list--left">
      <li>
        <svg class="contact-icon" viewBox="0 0 24 24" aria-hidden="true">
          <circle cx="12" cy="12" r="12" fill="#2b2b2b"/>
          <path d="M8.2 6.2c.4-.3 1-.3 1.3.1l1.4 2c.3.4.2.9-.1 1.2l-.8.7c.6 1.4 1.7 2.6 3.1 3.3l.7-.8c.3-.4.9-.4 1.2-.1l2 1.4c.4.3.5.9.1 1.3l-1 1.1c-.5.5-1.3.7-2 .4-3.3-1.3-5.8-3.9-7.1-7.2-.3-.7-.1-1.5.4-2z" fill="#fff"/>
        </svg>
        <span>401 726 3148</span>
      </li>
      <li>
        <svg class="contact-icon" viewBox="0 0 24 24" aria-hidden="true">
          <rect x="1" y="5" width="22" height="14" fill="#2b2b2b"/>
          <path d="M1.5 5.5 12 13.5 22.5 5.5" fill="none" stroke="#fff" stroke-width="1.4"/>
          <path d="M1.5 18.5 9 11.5M22.5 18.5 15 11.5" fill="none" stroke="#fff" stroke-width="1.2"/>
        </svg>
        <span>maplehollowbloompanels@mailvane.net</span>
      </li>
    </ul>

    <div class="contact-divider"></div>

    <ul class="contact-list contact-list--right">
      <li>
        <span class="social-mark" aria-hidden="true"></span>
        <span>handle-@maplehollowbloompanels</span>
      </li>
      <li>
        <span class="social-mark" aria-hidden="true"></span>
        <span>handle Handle- maplehollowbloompanels</span>
      </li>
    </ul>
  </section>

</main>
</body>
</html>
```